Landing page design for my current website

I need a landing page designed for my Wordpress website. My website is Plumvarick.com, and I need a page that will serve as a landing page for online ads I run. Please follow the color scheme of the current website

This web page will be targeted towards real estate owners who are looking for a property manager. Above the fold needs to have a CTA form headlined with "As a Rental Property Owner, I Want More Protection, Less Stress, and Drama-Free Living"

A few highlights that can be listed beyond the CTA and fold

- Comprehensive Property Management
Full-service management covering tenant placement, leasing, maintenance, and inspections.

Maximized Rental Income
Proven strategies to optimize rental rates and minimize vacancies, ensuring higher ROI.

Stress-Free Management
We handle all tenant interactions, maintenance requests, and property issues, so you don't have to.

Experienced Team
Over a decade of experience in managing single-family homes, small multifamily units, and apartment complexes.

Advanced Technology
Utilize cutting-edge property management software for efficient communication, rent collection, and maintenance tracking.

Tenant Screening and Placement
Thorough background checks and tenant screening processes to ensure reliable and responsible tenants.

Regular Property Inspections
Routine inspections to maintain property condition and address issues before they become costly problems.

Legal Compliance
Expertise in local and federal rental laws to keep your properties compliant and avoid legal hassles.

Transparent Reporting
Detailed monthly reports and financial statements to keep you informed about your property's performance.

Personalized Service
Tailored management plans to meet the unique needs of your properties and investment goals.
Effective Tenant Conflict Resolution
Skilled in handling challenging tenant situations, ensuring conflicts are resolved quickly and professionally to maintain a peaceful living environment and protect your investment.

```html
<!DOCTYPE html>
<html lang="en">
<head>
<meta charset="utf-8">
<title>Plumvarick Realty – Property Management</title>
<link href="https://fonts.googleapis.com/css2?family=Poppins:wght@400;500;600;700&family=Roboto:wght@300;400;500;700&display=swap" rel="stylesheet">
<style>
:root{
  --navy:#174a84;
  --navy-deep:#123f77;
  --footer:#0d1e3d;
  --wave:#1f56a0;
  --page:#eef0f3;
  --card:#ffffff;
  --icon-bg:#e6ebf2;
  --text:#222831;
  --muted:#9aa6ba;
  --line:#253a5f;
}
*{box-sizing:border-box;margin:0;padding:0}
html,body{width:1200px;height:2282px;overflow:hidden}
body{position:relative;background:var(--page);font-family:'Roboto',Arial,sans-serif;color:var(--text)}

.hero{position:absolute;left:0;top:0;width:1200px;height:720px}
.hero svg{display:block}
.brand{position:absolute;left:133px;top:34px;display:flex;align-items:center;gap:12px;color:#fff}
.brand-mark{width:52px;height:52px;border-radius:50%;border:3px solid #fff}
.brand-name{font-family:'Poppins',Arial,sans-serif;font-weight:700;font-size:28px;line-height:1;letter-spacing:.5px}

.lead-form{position:absolute;left:709px;top:46px;width:361px;height:558px;background:#fff;border-top:7px solid var(--navy);padding:30px 24px 0 33px;z-index:2}
.lead-form h1{font-family:'Poppins',Arial,sans-serif;font-weight:700;font-size:22.5px;line-height:27px;color:var(--navy);letter-spacing:-.2px}
.field{display:block;width:303px;height:41px;border:1px solid #1b1b1b;margin-top:10px;padding:0 13px;font-size:12.5px;line-height:39px;color:#222}
.field:first-of-type{margin-top:26px}
.submit{display:block;width:303px;height:50px;margin-top:16px;background:var(--navy);color:#fff;font-family:'Roboto',Arial,sans-serif;font-weight:500;font-size:19px;text-align:center;line-height:50px}

.features{position:absolute;left:133px;top:773px;width:939px;display:grid;grid-template-columns:299px 299px 299px;column-gap:21px;row-gap:19px}
.feature{background:var(--card);height:305px;text-align:center;padding-top:29px}
.feature .icon{width:71px;height:71px;border-radius:50%;background:var(--icon-bg);margin:0 auto;display:flex;align-items:center;justify-content:center}
.feature .icon svg{width:40px;height:40px;fill:none;stroke:var(--navy);stroke-width:1.6;stroke-linecap:round;stroke-linejoin:round}
.feature h2{font-family:'Poppins',Arial,sans-serif;font-weight:600;font-size:17.5px;line-height:26px;color:var(--navy);margin-top:20px}
.feature p{font-size:14px;line-height:19.3px;margin:14px auto 0;width:200px}
.feature.is-active{background:var(--navy-deep)}
.feature.is-active h2,.feature.is-active p{color:#fff}
.feature.is-active p{font-weight:300;width:218px}
.feature.is-active .icon{background:rgba(255,255,255,.12)}
.feature.is-active .icon svg{stroke:#fff}

.service{position:absolute;left:133px;top:1746px;width:939px;height:239px;background:#fff}
.service .icon{position:absolute;left:55px;top:45px;width:71px;height:71px;border-radius:50%;background:var(--icon-bg);display:flex;align-items:center;justify-content:center}
.service .icon svg{width:40px;height:40px;fill:none;stroke:var(--navy);stroke-width:1.6;stroke-linejoin:round;stroke-linecap:round}
.service h2{position:absolute;left:172px;top:39px;font-family:'Poppins',Arial,sans-serif;font-weight:600;font-size:17px;color:var(--navy)}
.service ul{position:absolute;left:172px;top:82px;width:690px;list-style:none}
.service li{position:relative;padding-left:23px;font-size:14px;line-height:19.5px;margin-bottom:14px}
.service li::before{content:"";position:absolute;left:1px;top:6px;width:9px;height:9px;border-radius:50%;background:var(--navy)}

.site-footer{position:absolute;left:0;top:2044px;width:1200px;height:238px;background:var(--footer);color:#fff}
.footer-brand{position:absolute;left:57px;top:45px;display:flex;align-items:center;gap:8px}
.footer-brand .mark{width:28px;height:28px;border-radius:50%;border:2px solid #fff}
.footer-brand span{font-family:'Poppins',Arial,sans-serif;font-weight:600;font-size:15px}
.footer-about{position:absolute;left:57px;top:96px;width:320px;font-family:'Poppins',Arial,sans-serif;font-size:9.6px;line-height:16px;color:var(--muted)}
.footer-about p+p{margin-top:9px}
.footer-divider{position:absolute;left:424px;top:25px;width:1px;height:200px;background:var(--line)}
.footer-rule{position:absolute;left:424px;top:177px;width:748px;height:1px;background:var(--line)}
.footer-col{position:absolute;top:43px}
.footer-col h3{font-family:'Poppins',Arial,sans-serif;font-weight:500;font-size:12.5px;margin-bottom:7px}
.footer-col a{display:block;font-family:'Poppins',Arial,sans-serif;font-size:10.5px;line-height:22.6px;color:var(--muted);text-decoration:none}
</style>
</head>
<body>

<header class="hero">
  <svg width="1200" height="720" viewBox="0 0 1200 720">
    <defs>
      <linearGradient id="heroPhoto" x1="0" y1="0" x2="0" y2="1">
        <stop offset="0" stop-color="#3f78c8"/>
        <stop offset=".35" stop-color="#9fbfe0"/>
        <stop offset=".55" stop-color="#b9a584"/>
        <stop offset=".82" stop-color="#a08d6c"/>
        <stop offset="1" stop-color="#5f9a35"/>
      </linearGradient>
      <clipPath id="heroClip">
        <path d="M0,0 H1200 V700 C1120,680 1020,650 900,645 C760,640 600,690 420,705 C300,715 200,700 0,612 Z"/>
      </clipPath>
    </defs>
    <rect width="1200" height="720" fill="var(--page)"/>
    <g clip-path="url(#heroClip)">
      <rect width="1200" height="720" fill="url(#heroPhoto)" role="img" aria-label="Photo of a two-storey tan suburban house with a white garage door and green lawn under a blue sky"/>
    </g>
    <path d="M0,612 C200,700 300,715 420,705 C600,690 760,640 900,645 C1020,650 1120,680 1200,700" fill="none" stroke="var(--wave)" stroke-width="12"/>
  </svg>
  <div class="brand">
    <div class="brand-mark"></div>
    <div class="brand-name">PLUMVARICK REALTY</div>
  </div>
</header>

<form class="lead-form">
  <h1>As a Rental Property Owner, I Want More Protection, Less Stress, and Drama-Free Living</h1>
  <span class="field">Full Name</span>
  <span class="field">Email Address</span>
  <span class="field">Phone Number</span>
  <span class="field">Property Address</span>
  <span class="field">Number of Units</span>
  <span class="field">Type of Property</span>
  <span class="submit">SUBMIT</span>
</form>

<section class="features">
  <article class="feature">
    <div class="icon"><svg viewBox="0 0 40 40"><path d="M12 16 L20 9 L28 16 V26 H12 Z"/><path d="M17 26 V20 H23 V26"/><path d="M5 20 C7 28 12 33 18 34 M35 20 C33 28 28 33 22 34"/></svg></div>
    <h2>Comprehensive<br>Property Management</h2>
    <p>Full-service management covering tenant placement, leasing, maintenance, and inspections.</p>
  </article>
  <article class="feature">
    <div class="icon"><svg viewBox="0 0 40 40"><circle cx="22" cy="13" r="7"/><path d="M22 9 V17 M24.5 10.5 H20.8 C19 10.5 19 13 20.8 13 H23.2 C25 13 25 15.5 23.2 15.5 H19.5"/><path d="M5 28 H12 L18 25 H26 C28 25 28 28 26 28 H19 M26 28 L33 24 C35 23 36 25 34.5 26.5 L26 33 H5"/></svg></div>
    <h2>Maximized<br>Rental Income</h2>
    <p>Proven strategies to optimize rental rates and minimize vacancies, ensuring higher ROI.</p>
  </article>
  <article class="feature">
    <div class="icon"><svg viewBox="0 0 40 40"><circle cx="20" cy="20" r="9"/><path d="M20 4 V8 M20 32 V36 M4 20 H8 M32 20 H36 M8.7 8.7 L11.5 11.5 M28.5 28.5 L31.3 31.3 M8.7 31.3 L11.5 28.5 M28.5 11.5 L31.3 8.7"/><circle cx="20" cy="20" r="4"/></svg></div>
    <h2>Stress-Free<br>Management</h2>
    <p>We handle all tenant interactions, maintenance requests, and property issues, so you don't have to.</p>
  </article>
  <article class="feature">
    <div class="icon"><svg viewBox="0 0 40 40"><rect x="6" y="24" width="28" height="4"/><path d="M9 28 V35 M31 28 V35"/><circle cx="20" cy="12" r="4"/><path d="M14 24 C14 19 26 19 26 24"/><circle cx="8" cy="15" r="3"/><circle cx="32" cy="15" r="3"/></svg></div>
    <h2>Experienced<br>Team</h2>
    <p>Over a decade of experience in managing single-family homes, small multifamily units, and apartment complexes.</p>
  </article>
  <article class="feature is-active">
    <div class="icon"><svg viewBox="0 0 40 40"><path d="M8 26 H32 L35 33 H5 Z"/><path d="M11 26 V14 M16 26 V10 M20 26 V16 M24 26 V10 M29 26 V14"/><circle cx="11" cy="12" r="2"/><circle cx="16" cy="8" r="2"/><circle cx="20" cy="14" r="2"/><circle cx="24" cy="8" r="2"/><circle cx="29" cy="12" r="2"/></svg></div>
    <h2>Advanced<br>Technology</h2>
    <p>Utilize cutting-edge property management software for efficient communication, rent collection, and maintenance tracking.</p>
  </article>
  <article class="feature">
    <div class="icon"><svg viewBox="0 0 40 40"><path d="M6 18 L18 7 L30 18"/><path d="M9 16 V34 H27 V16"/><rect x="12" y="20" width="5" height="5"/><rect x="20" y="20" width="5" height="5"/><path d="M30 34 V26 H35 V34"/></svg></div>
    <h2>Tenant Screening<br>and Placement</h2>
    <p>Thorough background checks and tenant screening processes to ensure reliable and responsible tenants.</p>
  </article>
  <article class="feature">
    <div class="icon"><svg viewBox="0 0 40 40"><path d="M5 18 L15 9 L25 18"/><path d="M8 16 V33 H22"/><circle cx="27" cy="22" r="6"/><path d="M31.5 26.5 L36 31"/></svg></div>
    <h2>Regular Property<br>Inspections</h2>
    <p>Routine inspections to maintain property condition and address issues before they become costly problems.</p>
  </article>
  <article class="feature">
    <div class="icon"><svg viewBox="0 0 40 40"><rect x="10" y="5" width="20" height="30" rx="2"/><circle cx="20" cy="13" r="3.5"/><path d="M14 21 H26 M14 25 H26 M14 29 H22"/></svg></div>
    <h2>Legal<br>Compliance</h2>
    <p>Expertise in local and federal rental laws to keep your properties compliant and avoid legal hassles.</p>
  </article>
  <article class="feature">
    <div class="icon"><svg viewBox="0 0 40 40"><rect x="10" y="9" width="20" height="26" rx="2"/><path d="M14 24 H26 M14 28 H26 M14 32 H22"/><circle cx="20" cy="16" r="4"/><circle cx="31" cy="9" r="4"/></svg></div>
    <h2>Transparent<br>Reporting</h2>
    <p>Detailed monthly reports and financial statements to keep you informed about your property's performance.</p>
  </article>
</section>

<section class="service">
  <div class="icon"><svg viewBox="0 0 40 40"><rect x="9" y="7" width="22" height="22" rx="1"/><circle cx="20" cy="15" r="4"/><path d="M13 23 H27"/><path d="M5 27 H35 V33 H5 Z"/></svg></div>
  <h2>Personalized Service</h2>
  <ul>
    <li>Tailored management plans to meet the unique needs of your properties and investment goals.</li>
    <li>Effective Tenant Conflict Resolution</li>
    <li>Skilled in handling challenging tenant situations, ensuring conflicts are resolved quickly and professionally to maintain a peaceful living environment and protect your investment.</li>
  </ul>
</section>

<footer class="site-footer">
  <div class="footer-brand"><div class="mark"></div><span>PLUMVARICK INC.</span></div>
  <div class="footer-about">
    <p>Plumvarick Property Management, based in Cedarvale, PA, is an innovative company dedicated to providing exceptional rental experiences.</p>
    <p>555.014.2290</p>
    <p>hello@Plumvarick.com</p>
  </div>
  <div class="footer-divider"></div>
  <div class="footer-rule"></div>
  <nav class="footer-col" style="left:470px">
    <h3>Main Links</h3>
    <a href="#">Home</a><a href="#">For Investors</a><a href="#">Residents</a><a href="#">Contact</a>
  </nav>
  <nav class="footer-col" style="left:750px">
    <h3>Service Areas</h3>
    <a href="#">Cedarvale</a><a href="#">Ashford Mills</a><a href="#">Larkspur</a><a href="#">Fenwick Falls</a>
  </nav>
  <nav class="footer-col" style="left:1030px">
    <h3>Other Resources</h3>
    <a href="#">Active Rentals</a><a href="#">Rent Pay</a>
  </nav>
</footer>

</body>
</html>
```